Design a box or sticker to be placed onto of a box for sports cards & other collectibles

We are starting up a business to sell limited edition sports collectibles, such as signed cards, jerseys, figurines etc online. Please refer to the blue box for reference on how the shape of the box will look like .

Design opaque stickers of GPX, Baseball, Football, Basketball, Moon Drift & RGT with a silhoutte/edgy feel to them.

Example: silhouette of a player playing the sports and the sport's ball or equipment to be coloured will look minimalistic and sleek. (For example: black figure with orange basket ball).

To ensure all our changes have been met. The GPX foil design is still not changed to look the same as the GPX sticker design.

Target Market(s)

Sports fans (basketball, soccer, football, baseball, wrestling etc), and collectible enthusiasts

Font styles to use
Other font styles liked:
• fonts should give off a "sporty" feel

Requirements
Must have
• Company logo without background (please remove the background), sleek design. The background colour is our company logo. +points if you are able to tastefully incorporate it into the design.
Nice to have
• open to discussion
Should not have
• open to discussion

```html
<!DOCTYPE html>
<html lang="en">
<head>
<meta charset="utf-8">
<title>Vantora Sports Collectibles – Box Front</title>
<link rel="stylesheet" href="https://fonts.googleapis.com/css2?family=Cinzel:wght@500&family=Saira+Condensed:wght@800&family=Chakra+Petch:wght@600;700&display=swap">
<style>
  :root{
    --page:#eceef1;
    --navy:#1b2130;
    --navy-side:#161b27;
    --green:#6dbb3a;
    --green-deep:#3f8a27;
    --white:#ffffff;
    --yellow:#e8cf63;
  }
  *{margin:0;padding:0;box-sizing:border-box;}
  html,body{width:1200px;height:859px;overflow:hidden;background:var(--page);}
  .canvas{position:relative;width:1200px;height:859px;}

  .box-side{
    position:absolute;left:285px;top:20px;width:110px;height:820px;overflow:hidden;
    background:linear-gradient(180deg,var(--navy-side) 0,var(--navy-side) 584px,var(--green-deep) 584px,#5aa232 820px);
  }
  .side-brand{
    position:absolute;left:55px;top:350px;
    transform:translate(-50%,-50%) rotate(-90deg);
    font-family:"Cinzel",serif;font-weight:500;font-size:40px;letter-spacing:1px;
    color:var(--white);white-space:nowrap;line-height:1;
  }
  .side-brand sup{font-size:.3em;vertical-align:top;margin-left:2px;}

  .box-front{
    position:absolute;left:395px;top:20px;width:520px;height:820px;
    overflow:hidden;background:var(--navy);
    font-family:"Chakra Petch",sans-serif;color:var(--white);
  }
  .box-art{position:absolute;inset:0;}
  .brand-small{
    position:absolute;left:181px;top:30px;line-height:1;
    font-family:"Cinzel",serif;font-weight:500;font-size:36px;letter-spacing:0;
  }
  .brand-small sup,.brand-large sup{font-size:.3em;vertical-align:top;margin-left:2px;}
  .title-sports{
    position:absolute;left:160px;top:66px;
    font-family:"Saira Condensed",sans-serif;font-weight:800;font-size:82px;line-height:1;
    color:var(--white);letter-spacing:-2px;
  }
  .title-collectibles{
    position:absolute;left:163px;top:142px;line-height:1;
    font-weight:700;font-size:21px;letter-spacing:1px;color:var(--green);
  }

  .tile{position:absolute;border-radius:16px;overflow:hidden;}
  .tile-cards{left:56px;top:302px;width:132px;height:200px;
    border:5px solid var(--white);border-left:none;border-bottom:none;border-radius:0 16px 0 0;}
  .tile-jerseys{left:184px;top:255px;width:140px;height:275px;
    border:5px solid var(--navy);border-top:none;border-right:none;border-radius:0 0 0 16px;
    background:linear-gradient(160deg,#9dbb5a,#c9c24a 45%,#6f9a3b);}
  .tile-figurines{left:327px;top:191px;width:160px;height:268px;
    border:5px solid var(--white);border-bottom:none;
    background:linear-gradient(170deg,#2d3a2c,#5a3a2a 45%,#8a3a22 70%,#2a2f28);}
  .ball{position:absolute;left:62px;top:392px;width:112px;height:112px;border-radius:50%;
    background:radial-gradient(circle at 35% 30%,#ffffff,#c9cdd2 70%,#8d9298);}

  .label{position:absolute;font-weight:700;color:var(--white);line-height:1;
    border:2px solid currentColor;border-right:none;border-bottom:none;padding:4px 6px;}
  .label-cards{left:87px;top:336px;font-size:20px;color:var(--navy);}
  .label-jerseys{left:210px;top:400px;font-size:22px;}
  .label-figurines{left:350px;top:302px;font-size:22px;}

  .brand-large{
    position:absolute;left:88px;top:646px;
    font-family:"Cinzel",serif;font-weight:500;font-size:66px;letter-spacing:0;line-height:1;
  }
  .tagline{position:absolute;left:146px;top:713px;font-size:11px;font-weight:600;display:flex;line-height:1;}
  .tagline .edition{color:var(--green);padding:3px 3px;}
  .tagline .collections{background:var(--green);color:var(--navy);padding:3px 5px;}
  .tags{position:absolute;left:156px;top:738px;display:flex;font-size:13px;font-weight:700;color:var(--navy);line-height:1;}
  .tags span{padding:5px 6px;}
  .tag-cards{background:var(--white);}
  .tag-jerseys{background:var(--yellow);}
  .tag-figurines{background:var(--green);}
</style>
</head>
<body>
<main class="canvas">
  <aside class="box-side">
    <div class="side-brand">VANTORA<sup>®</sup></div>
  </aside>

  <section class="box-front">
    <svg class="box-art" viewBox="0 0 520 820" width="520" height="820" aria-hidden="true">
      <defs>
        <linearGradient id="bandGreen" x1="0" y1="1" x2="1" y2="0">
          <stop offset="0" stop-color="#3f8a27"/>
          <stop offset=".5" stop-color="#7cc242"/>
          <stop offset="1" stop-color="#4d9a2e"/>
        </linearGradient>
      </defs>
      <rect width="520" height="820" fill="url(#bandGreen)"/>
      <path d="M0 0H520V132C380 160 200 190 0 215Z" fill="#1b2130"/>
      <path d="M0 820H520V410C380 470 200 540 0 584Z" fill="#1b2130"/>
      <path d="M0 6H520" stroke="#6dbb3a" stroke-width="5"/>
      <path d="M518 8L385 150Q375 162 358 163L150 176Q136 177 136 163V90" fill="none" stroke="#6dbb3a" stroke-width="5"/>
      <path d="M12 812L80 650Q88 630 108 622L420 530Q441 524 441 546V700" fill="none" stroke="#6dbb3a" stroke-width="5"/>
      <path d="M0 814H520" stroke="#6dbb3a" stroke-width="5"/>
    </svg>

    <div class="brand-small">VANTORA<sup>®</sup></div>
    <div class="title-sports">SPORTS</div>
    <div class="title-collectibles">COLLECTIBLES</div>

    <div class="tile tile-cards"></div>
    <div class="tile tile-jerseys" role="img" aria-label="Photo of a wrestler in a yellow singlet"></div>
    <div class="tile tile-figurines" role="img" aria-label="Photo of a basketball player holding a ball"></div>
    <div class="ball" role="img" aria-label="Soccer ball"></div>

    <div class="label label-cards">SIGNED<br>CARDS</div>
    <div class="label label-jerseys">JERSEYS</div>
    <div class="label label-figurines">FIGURINES</div>

    <div class="brand-large">VANTORA<sup>®</sup></div>
    <div class="tagline"><span class="edition">LIMITED EDITION</span><span class="collections">SPORTS COLLECTIONS</span></div>
    <div class="tags">
      <span class="tag-cards">SIGNED CARDS</span><span class="tag-jerseys">JERSEYS</span><span class="tag-figurines">FIGURINES</span>
    </div>
  </section>
</main>
</body>
</html>
```